Maskottchen für Reinigungsunternehmen
Zielgruppe
Wir sind ein Reinigungsunternehmen, dass sich derzeit auf Treppenhausreinigung und Büroreinigung beschränkt hat.
Die Zielgruppe sind zum Teil Privatpersonen, Unternehmen für die Büroreinigung in Frage kommt und Hausverwaltungen.
Aufgabenstellung
Es wäre schön, wenn hierbei ein Maskottchen kreiert wird, dass auf bestehenden Bilder hinzugefügt werden kann. Zudem soll das Maskottchen auch genäht werden, sodass wir ein physisches Exemplar nähen können. Das Maskottchen soll einen Wiedererkennungsmerkmal für das Unternehmen sein. Vergleichbar mit einem Logo. Es soll beispielsweise bei Monumenten zu sehen sein und überall mitgenommen werden.
Die Idee ist gegebenenfalls auch das Maskottchen irgendwann in einer größeren Menge produzieren zu lassen um es zum Beispiel zu spenden oder so.
Es soll hierbei nicht wie gewöhnlich ein Mensch zu sehen sein. Beispielsweise von unserem Konkurrenten im Ort: https://www.tarnovi.de/
Die Farbtöne unserer Internetseite sind wie folgt:
#1B93F6
#4CEF3F
Die Tiere und Fantasiewesen dürfen sehr gerne andere Farben haben. Wichtig ist nur das ein Element oder ggf. mehr einen der Farbtöne von unserer Homepage hat. Zum Beispiel, blaue Hände oder blaue Füße usw.
Bei weiteren Infos gerne kurz schreiben. - Danke -

```html
<!DOCTYPE html>
<html lang="de">
<head>
<meta charset="utf-8">
<title>Brisa Clean – Startseite und Maskottchen</title>
<link rel="stylesheet" href="https://fonts.googleapis.com/css2?family=Montserrat:wght@400;500;600;700&display=swap">
<style>
  :root{
    --navy:#1a2b8c;
    --brand-blue:#1b5fd6;
    --heading-blue:#1d4fc4;
    --brand-green:#4cef3f;
    --brand-teal:#3fb8a8;
    --text-dark:#3b3b3b;
    --text-mid:#6d6d6d;
    --text-light:#8a8a8a;
    --hero-bg-a:#ffffff;
    --hero-bg-b:#eceef1;
    --card-shadow:rgba(0,0,0,.12);
    --white:#ffffff;
  }
  *{box-sizing:border-box;margin:0;padding:0}
  html,body{width:927px;height:1200px;overflow:hidden;background:var(--white)}
  body{font-family:"Montserrat",sans-serif;color:var(--text-dark)}
  a{text-decoration:none}
  .canvas{position:relative;width:927px;height:1200px;overflow:hidden;background:var(--white)}

  .topbar{position:absolute;left:0;top:0;width:927px;height:30px}
  .topbar__contact{position:absolute;top:9px;font-size:9px;font-weight:600;color:var(--navy);display:flex;align-items:center;gap:4px}
  .topbar__contact--mail{left:103px}
  .topbar__contact--phone{left:275px}
  .topbar__social{position:absolute;right:82px;top:9px;display:flex;gap:11px}
  .topbar__dot{width:10px;height:10px;border-radius:50%;background:var(--navy)}

  .hero{position:absolute;left:8px;top:30px;width:919px;height:447px;background:linear-gradient(100deg,var(--hero-bg-a) 0%,var(--hero-bg-b) 100%)}

  .brand-box{position:absolute;left:82px;top:32px;width:187px;height:68px;background:var(--white);display:flex;align-items:center;gap:8px;padding-left:16px}
  .brand-box__square{width:32px;height:32px;background:var(--brand-blue)}
  .brand-box__name{font-size:20px;font-weight:700;color:var(--brand-blue);line-height:1}

  .mainnav{position:absolute;left:278px;top:32px;width:649px;height:56px;background:var(--navy);display:flex;align-items:center;padding-left:27px}
  .mainnav__link{font-size:11px;font-weight:600;color:var(--white);margin-right:40px}

  .hero__title{position:absolute;left:40px;top:176px;width:452px;text-align:center;font-size:28px;font-weight:700;color:var(--heading-blue);line-height:34px}
  .hero__text{position:absolute;left:36px;top:262px;width:460px;text-align:center;font-size:13px;line-height:19.5px;color:var(--text-mid)}
  .btn{position:absolute;top:350px;width:148px;height:27px;background:var(--navy);color:var(--white);font-size:11.5px;font-weight:500;display:flex;align-items:center;justify-content:center;border:1px solid #0f1c6a}
  .btn--book{left:117px}
  .btn--contact{left:274px}

  .mascot{position:absolute;border-radius:40% 40% 30% 30%}
  .mascot--hero{left:484px;top:104px;width:355px;height:368px;background:radial-gradient(ellipse at 60% 40%,#5cd24f 0%,#2a2a2a 55%,#f0f0f0 80%,transparent 82%)}
  .mascot--lockup{left:628px;top:914px;width:200px;height:226px;background:radial-gradient(ellipse at 40% 45%,#1b93f6 0%,#2a2a2a 55%,#f0f0f0 80%,transparent 82%)}

  .features__title{position:absolute;left:0;top:492px;width:927px;text-align:center;font-size:21px;font-weight:600;color:#444}
  .features__sub{position:absolute;left:0;top:526px;width:927px;text-align:center;font-size:10.5px;color:var(--text-light)}

  .card{position:absolute;top:575px;width:175px;height:329px;background:var(--white);box-shadow:0 2px 8px var(--card-shadow)}
  .card--home{left:95px}.card--office{left:290px}.card--hospital{left:486px}.card--car{left:681px}
  .card__photo{position:absolute;left:0;top:0;width:175px;height:173px;clip-path:polygon(0 0,100% 0,100% 88%,50% 100%,0 88%)}
  .card__photo--home{background:linear-gradient(160deg,#f3e6dc 0%,#c98856 60%,#8a4f2a 100%)}
  .card__photo--office{background:linear-gradient(160deg,#dfe6dd 0%,#3a63a8 55%,#e7e9ee 100%)}
  .card__photo--hospital{background:linear-gradient(160deg,#e9ecef 0%,#c8ccd2 55%,#2a7fc8 100%)}
  .card__photo--car{background:linear-gradient(160deg,#9aa3a8 0%,#2b3440 55%,#b9c6d0 100%)}
  .card__icon{position:absolute;left:72px;top:141px;width:31px;height:31px;border-radius:50%;background:var(--navy);display:flex;align-items:center;justify-content:center}
  .card__title{position:absolute;left:0;top:196px;width:175px;text-align:center;font-size:17px;font-weight:400;color:#555}
  .card__text{position:absolute;left:14px;top:224px;width:147px;text-align:center;font-size:10px;line-height:15.3px;color:var(--text-light)}

  .lockup__square{position:absolute;left:290px;top:1010px;width:130px;height:130px;background:var(--brand-blue)}
  .lockup__name{position:absolute;left:448px;top:1012px;font-size:48px;font-weight:700;color:var(--brand-blue);line-height:56px}
  .lockup__owner{position:absolute;left:450px;top:1128px;font-size:18px;font-weight:400;color:var(--brand-teal)}
</style>
</head>
<body>
<main class="canvas">

  <header class="topbar">
    <span class="topbar__contact topbar__contact--mail">
      <svg width="8" height="8" viewBox="0 0 8 8"><rect x=".5" y="1.5" width="7" height="5" fill="none" stroke="#1a2b8c"/><path d="M.5 1.5 4 4.5 7.5 1.5" fill="none" stroke="#1a2b8c"/></svg>
      kontakt@brisaclean-web.de
    </span>
    <span class="topbar__contact topbar__contact--phone">
      <svg width="8" height="8" viewBox="0 0 8 8"><rect x=".5" y=".5" width="7" height="7" rx="1" fill="none" stroke="#1a2b8c"/><path d="M2.5 2c0 2 1.5 3.5 3.5 3.5" fill="none" stroke="#1a2b8c"/></svg>
      +49 511 204 338
    </span>
    <div class="topbar__social" aria-label="Soziale Netzwerke">
      <span class="topbar__dot"></span><span class="topbar__dot"></span><span class="topbar__dot"></span><span class="topbar__dot"></span><span class="topbar__dot"></span>
    </div>
  </header>

  <section class="hero"></section>

  <div class="brand-box">
    <span class="brand-box__square"></span>
    <span class="brand-box__name">Brisa Clean</span>
  </div>

  <nav class="mainnav">
    <a class="mainnav__link" href="#">Home</a>
    <a class="mainnav__link" href="#">About Us</a>
    <a class="mainnav__link" href="#">Services</a>
    <a class="mainnav__link" href="#">Blog</a>
    <a class="mainnav__link" href="#">Pricing</a>
    <a class="mainnav__link" href="#">Contact Us</a>
  </nav>

  <h1 class="hero__title">We Promise keep you so<br>fresh and so Clean</h1>
  <p class="hero__text">Deploy your service infrastructure on our fully redundant,<br>high performance cloud platform and benefit from its high<br>reliability, security and enterprise feature set.</p>
  <a class="btn btn--book" href="#">Book Appointment</a>
  <a class="btn btn--contact" href="#">Contact Us</a>

  <div class="mascot mascot--hero" role="img" aria-label="Waschbär-Maskottchen mit grüner Mütze und grünem Shirt, hält einen Schrubber, daneben ein Putzeimer mit Reinigungsmitteln"></div>

  <h2 class="features__title">Latest Features &amp; Services</h2>
  <p class="features__sub">Take a look at some of latest features and services provided by our team</p>

  <article class="card card--home">
    <div class="card__photo card__photo--home" role="img" aria-label="Foto: Putzutensilien auf einem Holzboden"></div>
    <span class="card__icon"><svg width="13" height="13" viewBox="0 0 13 13"><rect x="1" y="3" width="11" height="9" fill="#fff"/><rect x="3" y="5" width="2" height="2" fill="#1a2b8c"/><rect x="8" y="5" width="2" height="2" fill="#1a2b8c"/><rect x="5.5" y="8" width="2" height="4" fill="#1a2b8c"/></svg></span>
    <h3 class="card__title">Home Cleaning</h3>
    <p class="card__text">High Performanc Lorem ipsum dolor sit amet, consectetur adipiscing consectetur adipiscing elit. Donec ut erat nec leo lobortis blandit.</p>
  </article>

  <article class="card card--office">
    <div class="card__photo card__photo--office" role="img" aria-label="Foto: Reinigungskraft mit Putzeimer und Besen"></div>
    <span class="card__icon"><svg width="13" height="13" viewBox="0 0 13 13"><circle cx="6.5" cy="4" r="2.5" fill="#fff"/><path d="M2 12c0-3 2-4.5 4.5-4.5S11 9 11 12z" fill="#fff"/></svg></span>
    <h3 class="card__title">Office Cleaning</h3>
    <p class="card__text">Lorem ipsum dolor sit amet, consectetur adipiscing elit. Donec ipsum dolor sit amet, consectetur ut erat nec leo lobortis blandit.</p>
  </article>

  <article class="card card--hospital">
    <div class="card__photo card__photo--hospital" role="img" aria-label="Foto: Reinigungskraft mit Putzwagen im Krankenhausflur"></div>
    <span class="card__icon"><svg width="13" height="13" viewBox="0 0 13 13"><rect x="1" y="4" width="11" height="7" rx="1" fill="#fff"/><rect x="4" y="2.5" width="5" height="2" fill="#fff"/><circle cx="6.5" cy="7.5" r="2" fill="#1a2b8c"/></svg></span>
    <h3 class="card__title">Hospit Cleaning</h3>
    <p class="card__text">Consectetur adipiscing elit. Lorem ipsum dolor sit amet, consectetur adipiscing elit. Donec ut erat nec leo lobortis blandit.</p>
  </article>

  <article class="card card--car">
    <div class="card__photo card__photo--car" role="img" aria-label="Foto: Mann poliert ein dunkles Auto"></div>
    <span class="card__icon"><svg width="13" height="13" viewBox="0 0 13 13"><rect x="1" y="4" width="11" height="7" rx="1" fill="#fff"/><rect x="4" y="2.5" width="5" height="2" fill="#fff"/><circle cx="6.5" cy="7.5" r="2" fill="#1a2b8c"/></svg></span>
    <h3 class="card__title">Car Cleaning</h3>
    <p class="card__text">Consectetur adipiscing elit. Lorem ipsum dolor sit amet, consectetur adipiscing elit. Donec ut erat nec leo lobortis blandit.</p>
  </article>

  <div class="mascot mascot--lockup" role="img" aria-label="Waschbär-Maskottchen mit blauem Shirt und Schrubber, daneben ein Putzeimer mit Reinigungsmitteln"></div>

  <section class="lockup">
    <span class="lockup__square"></span>
    <span class="lockup__name">Brisa<br>Clean</span>
    <span class="lockup__owner">Inh. Jonas Wieland</span>
  </section>

</main>
</body>
</html>
```